Editable A4 Flyer Template Design

We require an editable A4 flyer template design for our company Corvel Gasworks Ltd. We manufacture nitrogen gas generators which basically separate nitrogen from compressed air. Our products are used in scientific and industrial environments and worldwide.

Our logo is several shades of blue and we like this theme. The design should communicate our approachability whilst remaining professional.

Please visit our website www.corvel-gasworks.example.

There is a link to our Snapboard page which has some good images.

Target Market(s)

Business to business.

Laboratory Managers, Research Scientists, Buyers, Production Managers.

Industry/Entity Type

Industrial

Font styles to use
Serif
Sans Serif

Colors
0456a4
86acd3
3176b5
cfdfed

Requirements
Must have
• The flyers should be one single A4 sheet double sided.

```html
<!DOCTYPE html>
<html lang="en">
<head>
<meta charset="utf-8">
<title>N2 SteadyFlow Range – Corvel Gasworks Ltd.</title>
<link href="https://fonts.googleapis.com/css2?family=Oswald:wght@600;700&family=Cabin:wght@500&family=Arimo:wght@400&display=swap" rel="stylesheet">
<style>
  :root{
    --page-bg:#e9edf1;
    --sheet:#ffffff;
    --ink:#1b1b1b;
    --brand-deep:#0456a4;
    --brand-mid:#3176b5;
    --brand-soft:#86acd3;
    --brand-pale:#cfdfed;
    --sky:#4fb8e6;
    --sky-pale:#dff1fa;
  }
  html,body{margin:0;padding:0;width:1200px;height:1000px;overflow:hidden;background:var(--page-bg);}
  .flyer{position:absolute;left:245px;top:0;width:710px;height:1000px;background:var(--sheet);overflow:hidden;}
  .flyer__art{position:absolute;inset:0;}
  .flyer__title{position:absolute;left:15px;top:30px;margin:0;font-family:"Oswald",sans-serif;font-weight:700;font-size:66px;line-height:1;color:var(--ink);letter-spacing:-0.5px;white-space:nowrap;}
  .flyer__title sub{font-size:34px;line-height:0;vertical-align:-16px;margin-right:8px;}
  .flyer__tagline{position:absolute;left:13px;top:164px;margin:0;font-family:"Cabin",sans-serif;font-weight:500;font-size:29.5px;line-height:48px;color:var(--brand-deep);letter-spacing:-0.4px;white-space:nowrap;}
  .flyer__intro{position:absolute;left:14px;top:298px;width:548px;margin:0;font-family:"Arimo",sans-serif;font-size:22.5px;line-height:33.4px;color:var(--ink);}
  .flyer__intro sub{font-size:13px;line-height:0;vertical-align:-4px;}
  .features{position:absolute;left:66px;top:720px;}
  .features__heading{margin:0 0 4px 18px;font-family:"Oswald",sans-serif;font-weight:600;font-size:31px;line-height:1.2;color:var(--brand-deep);letter-spacing:-0.3px;}
  .features__list{list-style:none;margin:0;padding:0;font-family:"Arimo",sans-serif;font-size:24.5px;line-height:29.7px;color:var(--ink);}
  .features__list li::before{content:"•";display:inline-block;width:13px;font-size:16px;vertical-align:3px;}
  .features__list sup{font-size:13px;line-height:0;vertical-align:9px;}
  .product-photo{position:absolute;left:423px;top:603px;width:254px;height:254px;border-radius:50%;border:6px solid var(--brand-mid);box-sizing:border-box;
    background:
      radial-gradient(circle at 40% 42%,rgba(214,60,70,0.55) 0%,rgba(214,60,70,0) 22%),
      radial-gradient(circle at 68% 38%,rgba(214,60,70,0.55) 0%,rgba(214,60,70,0) 20%),
      linear-gradient(180deg,#cfc8bc 0%,#b8b0a3 40%,#8b8f9c 75%,#5b6478 100%);}
</style>
</head>
<body>
<main class="flyer">
  <svg class="flyer__art" width="710" height="1000" viewBox="0 0 710 1000" aria-hidden="true">
    <defs>
      <linearGradient id="skyFill" x1="0" y1="0" x2="0" y2="1">
        <stop offset="0" stop-color="#ffffff"/>
        <stop offset="0.35" stop-color="#eaf6fc"/>
        <stop offset="1" stop-color="#4fb8e6"/>
      </linearGradient>
      <linearGradient id="bandFill" x1="0" y1="0" x2="1" y2="1">
        <stop offset="0" stop-color="#3a8fd6"/>
        <stop offset="0.5" stop-color="#0e63b5"/>
        <stop offset="1" stop-color="#1d7cc8"/>
      </linearGradient>
      <linearGradient id="swooshFill" x1="0" y1="0" x2="1" y2="0">
        <stop offset="0" stop-color="#0b5cab"/>
        <stop offset="1" stop-color="#2b86cf"/>
      </linearGradient>
    </defs>
    <path class="sky-panel" d="M505,-10 C690,70 730,320 600,520 C530,630 590,850 690,1010 L720,1010 L720,-10 Z" fill="url(#skyFill)"/>
    <g class="bubbles" fill="#ffffff" opacity="0.22">
      <circle cx="680" cy="520" r="16"/><circle cx="690" cy="580" r="22"/>
      <circle cx="640" cy="610" r="12"/><circle cx="700" cy="660" r="28"/>
      <circle cx="600" cy="900" r="20"/><circle cx="660" cy="940" r="26"/>
      <circle cx="640" cy="860" r="14"/><circle cx="560" cy="960" r="18"/>
    </g>
    <path class="main-band" d="M505,-10 C690,70 730,320 600,520 C530,630 590,850 690,1010" fill="none" stroke="url(#bandFill)" stroke-width="42"/>
    <path class="lower-swoosh" d="M-10,735 C110,650 320,625 470,665" fill="none" stroke="url(#swooshFill)" stroke-width="22"/>
  </svg>

  <h1 class="flyer__title">N<sub>2</sub>SteadyFlow Range</h1>

  <p class="flyer__tagline">Up to 150 l/min of laboratory grade nitrogen…<br>perfect for supplying multiple instruments.</p>

  <p class="flyer__intro">Why go through all the hassle of ordering, taking delivery and connecting bottle after bottle when our nitrogen generators can do all the hard work for you?<br>N<sub>2</sub> Stream generators are specifically designed to supply laboratory and industrial instrumentation and lead to improved process quality, reduced equipment downtime and lower operation costs.</p>

  <div class="product-photo" role="img" aria-label="Close-up photo of generator pressure gauges with red digital displays and blue air tubing"></div>

  <section class="features">
    <h2 class="features__heading">Features &amp; Benefits:</h2>
    <ul class="features__list">
      <li>Health &amp; Safety friendly</li>
      <li>Dew point &lt; -30<sup>o</sup>C</li>
      <li>Consistent supply of nitrogen</li>
      <li>Low cost maintenance</li>
      <li>Quiet</li>
      <li>Plug &amp; Play</li>
      <li>Two year Warranty</li>
    </ul>
  </section>
</main>
</body>
</html>
```